Brisk Hollow Builders Needs A Flyer

We need a flyer for our newest product "The Cedarlane Garden Workroom"

Here is some copy for the flyer:

1. More and more people everyday are working from home and finding it difficult to disconnect from home activities in order to focus on their work. They are also finding it very expensive to add on to their existing house for a quiet place. Our archatectually stunning, Cedarlane Garden Workroom is the answer. The office studio measures 16' wide and 10' deep. 160 Square feet of space.

Perfect for dozens of purposes. Home office, design studio, artist studio, home school office, reading room, craft studio, drafting room.

Features include:

- Steel Framing. 40-60% lighter then wood, higher strength to weight ratio, resistant to mold and fire and steel is the most recycled material on earth!
- Spray foam insulation. Cool in the summer and warm in the winter.
- HVAC Mini Split with wireless remote control and thermostat.
- 100% Off grid with enough solar and battery storage to run your entire office. No need to pay for an expensive electric installation.
- Flush fitting floor outlets to reduce wires.
- TV mount (Optional with pre-wired electric, HDMI, digital audio & Cat 6)
- Windows are tempered glass custom made by Morvik Glazing.
- Solar qualifies for a 26% tax credit. This is not a write-off rather it is a direct reduction on your tax obligation.
- Thousands of dollars less than adding onto your home.
- Custom color, siding, features available.

This beautiful back yard office is delivered 100% assembled and ready to enjoy on the day of delivery.

We ship nationwide from our factory in South Carolina. Give us a call anytime to speak to a designer and start your dream office today!

555-318-4027
info@BriskHollowBuilders.example

```html
<!DOCTYPE html>
<html lang="en">
<head>
<meta charset="utf-8">
<title>The Cedarlane Garden Workroom — Brisk Hollow Builders</title>
<link href="https://fonts.googleapis.com/css2?family=Archivo+Black&family=Noto+Sans:wght@700;800&display=swap" rel="stylesheet">
<style>
  :root {
    --cyan: #00f5f7;
    --teal-top: #14cccc;
    --teal-bottom: #0a8486;
    --ink: #000000;
    --paper: #ffffff;
    --photo-sky: #a9c6d8;
    --photo-wall: #3c3f41;
    --photo-warm: #d8cfc2;
    --photo-wood: #b08a5e;
  }
  * { margin: 0; padding: 0; box-sizing: border-box; }
  html, body { width: 1200px; height: 1200px; overflow: hidden; background: var(--paper); }
  .stage { position: relative; width: 1200px; height: 1200px; }
  .flyer {
    position: absolute; left: 152px; top: 20px;
    width: 1296px; height: 1678px;
    transform: scale(0.6913); transform-origin: 0 0;
    background: linear-gradient(180deg, var(--teal-top) 0%, #0fb3b4 45%, var(--teal-bottom) 100%);
    overflow: hidden;
    font-family: "Noto Sans", Verdana, sans-serif;
    font-weight: 800;
  }
  .hero-shapes { position: absolute; left: 0; top: 0; }
  .title {
    position: absolute; right: 24px; top: 30px; width: 540px;
    font-family: "Archivo Black", "Arial Black", sans-serif;
    font-weight: 400;
    font-size: 70px; line-height: 73px; text-align: right;
    color: var(--ink); text-transform: uppercase; white-space: nowrap;
  }
  .intro {
    position: absolute; right: 18px; top: 353px; width: 860px;
    color: var(--paper); font-size: 29px; line-height: 45.8px;
    text-align: right; letter-spacing: 0.6px; white-space: nowrap;
  }
  .purposes {
    position: absolute; left: 340px; top: 820px; width: 940px;
    text-align: center; color: var(--ink);
    font-size: 26px; line-height: 37px; letter-spacing: 0.8px; text-transform: uppercase;
    white-space: nowrap;
  }
  .features { position: absolute; left: 16px; top: 926px; width: 940px; }
  .features-heading { font-size: 32px; line-height: 42px; color: var(--ink); font-weight: 800; }
  .feature-list {
    list-style: none; color: var(--paper);
    font-size: 24px; line-height: 31.6px; letter-spacing: 0.6px; white-space: nowrap;
  }
  .contact-band {
    position: absolute; left: 0; top: 1565px; width: 946px; height: 113px;
    background: var(--cyan); padding: 2px 12px 0; color: var(--ink);
    font-size: 46px; line-height: 54px; font-weight: 800; white-space: nowrap;
  }
  .cta {
    position: absolute; right: 18px; top: 1054px; width: 300px;
    text-align: right; color: var(--ink);
    font-size: 33px; line-height: 46.5px; letter-spacing: 0.4px; white-space: nowrap;
  }
</style>
</head>
<body>
<main class="stage">
  <article class="flyer">
    <svg class="hero-shapes" width="1296" height="1678" viewBox="0 0 1296 1678">
      <defs>
        <linearGradient id="exterior-tones" x1="0" y1="0" x2="0" y2="1">
          <stop offset="0" stop-color="#a9c6d8"/>
          <stop offset="0.35" stop-color="#5e6a5a"/>
          <stop offset="0.75" stop-color="#3c3f41"/>
          <stop offset="1" stop-color="#7c8a66"/>
        </linearGradient>
        <linearGradient id="interior-tones" x1="0" y1="0" x2="1" y2="0">
          <stop offset="0" stop-color="#b08a5e"/>
          <stop offset="0.4" stop-color="#d8cfc2"/>
          <stop offset="1" stop-color="#c9c2b8"/>
        </linearGradient>
      </defs>
      <polygon points="690,0 710,0 710,318 360,506 0,300 0,290" fill="var(--cyan)"/>
      <polygon points="0,840 300,950 365,812 1296,812 1296,976 300,976 0,860" fill="var(--cyan)"/>
      <polygon points="0,330 355,520 400,712 300,952 0,848" fill="var(--cyan)"/>
      <polygon points="980,1080 1296,976 1296,1678 980,1678" fill="var(--cyan)"/>
      <polygon role="img" aria-label="Exterior photo of the garden workroom with tall glass walls, set among trees"
               points="0,0 688,0 688,310 355,497 0,290" fill="url(#exterior-tones)"/>
      <polygon role="img" aria-label="Interior photo of the workroom's wooden glass doors and globe pendant light"
               points="0,348 340,527 380,712 290,945 0,840" fill="url(#interior-tones)"/>
    </svg>

    <h1 class="title">The<br>Cedarlane<br>Garden<br>Workroom</h1>

    <p class="intro">More and more people everyday are<br>working from home and finding it<br>difficult to disconnect from home<br>activities in order to focus on their<br>work. They are also finding it very expensive<br>to add on to their existing house for a quiet<br>place. Our archatectually stunning, Cedarlane<br>Garden Workroom is the answer.<br>The office studio measures 16' wide and 10'<br>deep. 160 Square feet of space.</p>

    <p class="purposes">Perfect for dozens of purposes.<br>Home office, design studio, artist studio,<br>home school office, reading room, craft studio,<br>drafting room</p>

    <section class="features">
      <h2 class="features-heading">Features<br>include:</h2>
      <ul class="feature-list">
        <li>- Steel Framing. 40-60% lighter then wood, higher strength<br>to weight ratio, resistant to mold and fire and steel is the<br>most recycled material on earth!</li>
        <li>- Spray foam insulation. Cool in the summer and warm<br>in the winter.</li>
        <li>- HVAC Mini Split with wireless remote control and thermostat.</li>
        <li>- 100% Off grid with enough solar and battery storage to run<br>your entire office. No need to pay for an expensive electric<br>installation.</li>
        <li>- Flush fitting floor outlets to reduce wires.</li>
        <li>- TV mount (Optional with pre-wired electric, HDMI,<br>digital audio &amp; Cat 6)</li>
        <li>- Windows are tempered glass custom made by Morvik Glazing.</li>
        <li>- Solar qualifies for a 26% tax credit. This is not a write-off<br>rather it is a direct reduction on your tax obligation.</li>
        <li>- Thousands of dollars less than adding onto your home.</li>
        <li>- Custom color, siding, features available.</li>
      </ul>
    </section>

    <div class="contact-band">
      <p class="contact-phone">555-318-4027</p>
      <p class="contact-email">info@BriskHollowBuilders.example</p>
    </div>

    <p class="cta">We ship<br>nationwide<br>from our<br>factory in<br>South<br>Carolina.<br>Give us a call<br>anytime to<br>speak to a<br>designer<br>and start<br>your dream<br>office today!</p>
  </article>
</main>
</body>
</html>
```